My dad's 70th birthday party invite - Greek theme!

My dad isn't actually Greek, but his party will be at a Greek restaurant, so we thought it'd be a fun to have a Greek theme for the invitation to his 70th birthday party.

The invite will be sent out by email, so it needs to look good on screen, AND when it's printed out by the recipients, likely onto A4 paper and put up on a noticeboard/stuck to the fridge as a reminder etc.
Updates

Reason: A designer has asked us to extend the deadline and as we're not in a rush to complete this particular project, we've done so. Thanks everyone for their designs to date.

Target Market(s)

my dad's friends and family - average 50-70years old

Industry/Entity Type

Restaurant

Requirements
Must have
• For: Brannick's 70th birthday
Date: 30 Nov 2013
Time: 7.30pm
Place: Lymora Taverna, 47 Tressendale Road, Mulvaney Park

RSVP by: Friday 1 November
to: kat@pqx-example.com.au
(Please also let us know of any specific dietary requirements eg vegetarian, seafood allergy etc. Thanks. And please, no presents - just really hoping you can join us on the night!)
Nice to have
• Some ideas for you:
- he loves the blue & white of Greece eg white buildings against blue ocean, Greek flag etc
- and red geraniums/pink bouganvillea - quintessential (yet stylish!) Greece
- also, maybe you could use the names of the dishes we'll be having for dinner somehow? ie:
MEZES
Taramosalata
Tzatziki
Skordalia
Hommus
Haloumi
Psití Melitzána
Pita
Eliés
Dolmathes
THALASINA
Chtapódi Psitó
KalamáriaTiganitá
KREATA
Souvlaki
Arní
Lachaniká se Sáltsa - Verrosti
SALATA
Baklava
Paximádi Rolá
Kataifi
Kourabiethes
Greek Coffee

Hope that helps!
Should not have
• We'd prefer a simple colour scheme, ie not too many different colours.

```html
<!DOCTYPE html>
<html lang="en">
<head>
<meta charset="utf-8">
<title>Brannick's 70th Birthday</title>
<link rel="stylesheet" href="https://fonts.googleapis.com/css2?family=Cinzel:wght@400;600&display=swap">
<style>
  :root {
    --aegean: #1d6cb5;
    --aegean-soft: #2f7bc0;
    --aegean-mist: #3a84c6;
    --white: #ffffff;
    --band-light: #e8f0f8;
    --band-mid: #c9dcef;
  }
  html, body {
    margin: 0;
    padding: 0;
    overflow: hidden;
  }
  body {
    width: 832px;
    height: 1200px;
  }
  .invite {
    position: relative;
    width: 832px;
    height: 1200px;
    background: var(--aegean);
    overflow: hidden;
    font-family: "Cinzel", "Trajan Pro", serif;
    color: var(--white);
  }

  /* Menu texture area behind the details */
  .menu-texture {
    position: absolute;
    left: 0;
    top: 264px;
    width: 832px;
    height: 712px;
    background: linear-gradient(180deg,
      var(--aegean) 0%,
      var(--aegean-soft) 12%,
      var(--aegean-mist) 50%,
      var(--aegean-soft) 88%,
      var(--aegean) 100%);
  }

  /* Foreground lines */
  .line {
    position: absolute;
    left: 0;
    width: 100%;
    margin: 0;
    text-align: center;
    line-height: 1;
    font-weight: 400;
    white-space: nowrap;
    transform: translateY(-50%);
  }
  .lead { top: 47px; font-size: 43px; }
  .honoree { top: 116px; font-size: 86px; }
  .occasion { top: 205px; font-size: 118px; letter-spacing: 1px; }

  .when { font-size: 37px; }
  .when-date { top: 376px; }
  .when-time { top: 416px; }

  .label { font-size: 31px; }
  .place-label { top: 494px; }
  .place-detail { top: 529px; font-size: 27px; }
  .rsvp-label { top: 596px; }
  .rsvp-detail { font-size: 25px; }
  .rsvp-by { top: 634px; }
  .rsvp-to { top: 667px; }
  .dietary { font-size: 23.5px; }
  .dietary-1 { top: 729px; }
  .dietary-2 { top: 760px; }

  .closing { font-size: 40px; }
  .closing-1 { top: 852px; }
  .closing-2 { top: 894px; }
  .closing-3 { top: 935px; }

  /* Decorative border band */
  .border-band {
    position: absolute;
    left: 0;
    top: 1000px;
    width: 832px;
    height: 200px;
    background: var(--aegean);
  }
  .border-band .rule {
    position: absolute;
    left: 0;
    width: 100%;
    height: 4px;
    background: var(--white);
  }
  .border-band .rule-top { top: 0; }
  .border-band .rule-bottom { bottom: 4px; }
  .border-band .ornament {
    position: absolute;
    left: 0;
    top: 10px;
    width: 100%;
    height: 176px;
    background: linear-gradient(180deg, var(--band-light) 0%, var(--band-mid) 55%, var(--band-light) 100%);
  }
</style>
</head>
<body>
<main class="invite">

  <div class="menu-texture" role="img" aria-label="Faint background texture of Greek dinner menu dish names in lighter blue"></div>

  <header>
    <p class="line lead">Please Join us to celebrate</p>
    <h1 class="line honoree">Brannick's 70th</h1>
    <p class="line occasion">Birthday</p>
  </header>

  <section class="details">
    <p class="line when when-date">On 30th November, 2013</p>
    <p class="line when when-time">At 7.30pm</p>

    <p class="line label place-label">Place</p>
    <p class="line place-detail">Lymora Taverna, 47 Tressendale Road</p>

    <p class="line label rsvp-label">RSVP</p>
    <p class="line rsvp-detail rsvp-by">by: Friday 1 November</p>
    <p class="line rsvp-detail rsvp-to">to: kat@pqx-example.com.au</p>

    <p class="line dietary dietary-1">(Please also let us know of any specific dietary</p>
    <p class="line dietary dietary-2">requirements eg vegetarian, seafood allergy etc.)</p>
  </section>

  <footer>
    <p class="line closing closing-1">Thanks. And please, no</p>
    <p class="line closing closing-2">presents - just really hoping</p>
    <p class="line closing closing-3">you can join us on the night!)</p>
  </footer>

  <div class="border-band">
    <div class="rule rule-top"></div>
    <div class="ornament" role="img" aria-label="Greek palmette and scroll border ornament in blue and white"></div>
    <div class="rule rule-bottom"></div>
  </div>

</main>
</body>
</html>
```